Fern Assembly Business Cards

Looking or a business card design for my start-up, called "Fern Assembly".
Our tagline is "Unleashing the human potential for good through leadership, culture, and education."
Our mission-driven work includes professional/personal development workshops, educational design services, organizational & project management consulting, and coaching services for K-12 schools, organizations, and individuals.
You can check out the website we're building at fernassembly.example
I select projects from designers who are highly responsive to feedback, engage in dialog about revisions, and provide all root/source documents (so please state in your initial submission that you agree to do so).
Looking forward to seeing your great designs!!
Updates
Hello everyone,
Industry/Entity Type
Building
Requirements
Must have
- Looking for a two sided design that includes our logo (I am uploading two variations that I would like incorporated in .ai format) and website on both sides.
The front side must include:
Logo, Name, Title, Phone, Email, Twitter handle
The back side must include: Logo, @fernassem (our organizational twitter handle)
Nice to have
- I like the rounded corner business cards, but that is not absolutely essential.
Should not have
- Colors beyond those presented in our logo.

```html
<!DOCTYPE html>
<html lang="en">
<head>
<meta charset="utf-8">
<title>Fern Assembly – Business Cards</title>
<link href="https://fonts.googleapis.com/css2?family=Libre+Baskerville&display=swap" rel="stylesheet">
<style>
  :root {
    --backdrop: #4a4a4a;
    --card: #050505;
    --sky: #6ccbe0;
    --stone: #bdb6ae;
    --ink: #0a0a0a;
    --muted: #b8b2ab;
  }
  * { margin: 0; padding: 0; box-sizing: border-box; }
  html, body { width: 1200px; height: 900px; overflow: hidden; }
  body {
    background: var(--backdrop);
    font-family: "Libre Baskerville", "Times New Roman", serif;
    position: relative;
  }
  .card {
    position: absolute;
    top: 301px;
    width: 524px;
    height: 299px;
    background: var(--card);
    border-radius: 22px;
    overflow: hidden;
  }
  .card--front { left: 63px; }
  .card--back { left: 612px; }

  .brand-dot {
    position: absolute;
    border-radius: 50%;
    background: var(--sky);
  }
  .card--front .brand-dot { left: 116px; top: 26px; width: 60px; height: 60px; }
  .card--back .brand-dot { left: 213px; top: 30px; width: 98px; height: 98px; }

  .wordmark {
    position: absolute;
    left: 0; width: 292px;
    text-align: center;
    color: var(--stone);
    text-transform: uppercase;
    white-space: nowrap;
  }
  .card--front .wordmark { top: 103px; font-size: 18px; letter-spacing: 1px; }
  .pillars {
    position: absolute; left: 0; width: 292px; top: 125px;
    text-align: center; color: var(--muted);
    font-size: 6px; letter-spacing: 3px; text-transform: uppercase;
  }
  .site-small {
    position: absolute; left: 0; width: 292px; top: 137px;
    text-align: center; color: var(--muted); font-size: 5px;
  }
  .person { position: absolute; left: 31px; top: 160px; }
  .person__name { color: var(--sky); font-size: 18px; line-height: 24px; }
  .person__title { color: var(--muted); font-size: 12px; line-height: 16px; }
  .contact { position: absolute; left: 31px; top: 215px; color: var(--muted); font-size: 12.5px; line-height: 17px; }
  .handle {
    position: absolute; left: 31px; top: 255px;
    display: flex; align-items: center; gap: 6px;
    background: var(--sky); color: var(--ink);
    font-size: 12.5px; line-height: 18px;
    padding: 0 6px; border-radius: 4px;
  }
  .handle__dot { width: 10px; height: 10px; border-radius: 50%; background: var(--ink); }

  .card--back .wordmark { left: 0; width: 524px; top: 172px; font-size: 28px; letter-spacing: 1px; }
  .tagline {
    position: absolute; left: 0; width: 524px; top: 203px;
    text-align: center; color: var(--muted);
    font-size: 10px; line-height: 12px; letter-spacing: 1.4px; text-transform: uppercase;
  }
  .site-pill {
    position: absolute; left: 153px; top: 244px; width: 218px; height: 24px;
    background: var(--sky); color: var(--ink); border-radius: 4px;
    font-size: 14px; line-height: 24px; text-align: center;
  }
</style>
</head>
<body>
  <section class="card card--front">
    <div class="brand-dot"></div>
    <div class="wordmark">Fern Assembly</div>
    <div class="pillars">Leadership | Culture | Education</div>
    <div class="site-small">www.fernassembly.example</div>
    <div class="person">
      <div class="person__name">Mara Ellison</div>
      <div class="person__title">Owner</div>
    </div>
    <div class="contact">
      <div>p: 888 555 0142</div>
      <div>e: mara@fernassembly.example</div>
    </div>
    <div class="handle"><span class="handle__dot"></span>follow @fernassem</div>
  </section>

  <section class="card card--back">
    <div class="brand-dot"></div>
    <div class="wordmark">Fern Assembly</div>
    <div class="tagline">Unleashing the human potential for good through<br>leadership, culture, and education</div>
    <div class="site-pill">www.fernassembly.example</div>
  </section>
</body>
</html>
```